Corvessa Print Package_Logo/TriFold and Business Card

Need a trifold brochure designed, as well as a logo, and business card with a back side for appointment reminders. The business is an OBGYN, catering to all females and a thorough intake document will be attached for all design direction.

Further details on the client = SHE Glow clinic is a Nashville's first gynecology office to provide the Velora Gentle minimally invasive and non pharmacologic treatment of vaginal dryness/atrophy.

In addition to the Velora Gentle therapy, Dr. Corvessa offers many pharmacologic treatment options, therapeutic alternatives and holistic approaches to patients suffering with HSDD ( Hypoactive Sexual Desire Disorder), FSAID (Female Sexual Arousal/Interest Disorder), orgasmic disorders and more.

Dr. Corvessa has dedicated her practice to helping women in all phases of their sexual well being and is proud to offer this unique and novel approach which will be a welcome treatment options for many patients in and around Middle Tennessee.
About Our Doctor
Delphine Corvessa
Female
Marlowe Institute at Fennick
Ashgrove University, Nashville
Ashgrove
Nashville, Tennessee
Dr. Corvessa is a native of California and attended MI, Fennick. Upon graduation from medical school at Ashgrove University, she completed her residency in obstetrics and gynecology. Dr. Corvessa is a Fellow of the National Guild of Prenatal and Pelvic Care and has expanded her practice most recently to include all aspects of female sexual dysfunction. Offering individualized treatment plans focused on her patient's specific issues, she has a full array of diagnosis, treatment and rehabilitative options.
Dr. Corvessa is also a Fellow of QPTRAL and recently completed her preceptorship with Dr. Gordon Palewski, Executive Medical Director for the Coastal Ridge Institute for Intimate Wellness and Recovery Medicine.
Establishing her practice as the premier institute in Nashville for women suffering with sexual dysfunction and offering a safe, comprehensive place to discuss and address these issues is a natural progression of her experience with and interest in sexual medicine.

Other Services
Hormone Replacement Therapy Consult
Sexual Dysfunction Evaluation and Treatment

Please Note: the logo image that is uploaded was just something quick sent by the client and is not great, it is mostly just She Glow in script with the W and H larger. They are an OBGYN practice and we would like to logo to appear professional, yet playful.

Content for these designs should be taken from these two reference websites: http://www.brindlecovelaserspa.example/
http://pvtrellisglow.example/

This template will be used for the client's overall website. Please reference color scheme, etc.http://sitedraftbox.example/stage/velorag2/

Email address to be put on brochure - sheglow@pabst-corvessa.example

Target Market(s)

female

Industry/Entity Type

Business

Contact Information for Business Card

There is an example attached, however for this project we would like for the business card to be more business oriented, ie: with a name, email address, title on the front and the appointment reminder on the back.

Information for front of card:
Dr. Delphine Corvessa
718 Larkspur Rd. Suite 412
Nashville, TN 37299
1-877-SHE-GLOW

Logo Text

She Glow with a tagline of Letting SHE Find Her Bright Spark

Font styles to use
Script

Requirements
Must have
• Image / logo of the VeloraGentle Laser, which can be found here:
• http://www.quellant.example/product/velora-gentle/
• Practice Name / Details:
• SHE Glow
• 618 Larkspur Road Suite 412
• Nashville
• TN
• 877-SHE-GLOW(743-4569)
• tbrevinshaw@mailpost.example
• tristarveloragentle.example
• Client Demographics = (for selection of images)
• Ages 35-45, 45-55
• Caucasian, African American, Hispanic or Latino, Asian

```html
<!DOCTYPE html>
<html lang="en">
<head>
<meta charset="utf-8">
<title>She Glow – Appointment Card</title>
<link rel="stylesheet" href="https://fonts.googleapis.com/css2?family=Josefin+Sans:wght@300&display=swap">
<style>
  :root {
    --blush: #f4b6cf;
    --stone: #d4cfc5;
    --ink: #3b3b3b;
    --paper: #ffffff;
  }
  * { margin: 0; padding: 0; box-sizing: border-box; }
  html, body {
    width: 1200px; height: 248px; overflow: hidden;
    background: var(--paper);
    font-family: "Josefin Sans", sans-serif;
    font-weight: 300;
    color: var(--ink);
  }
  .sheet { position: relative; width: 1200px; height: 248px; }

  /* Back side: appointment reminder */
  .card-back { position: absolute; left: 0; top: 0; width: 392px; height: 248px; }
  .side-band {
    position: absolute; left: 0; top: 0; width: 34px; height: 248px;
    background: var(--blush);
  }
  .side-band .dot {
    position: absolute; left: 12px; top: 8px; width: 10px; height: 10px;
    border-radius: 50%; background: var(--stone);
  }
  .side-band .brand {
    position: absolute; left: 17px; top: 128px;
    transform: translate(-50%, -50%) rotate(-90deg);
    white-space: nowrap; color: var(--paper); font-size: 32px; line-height: 1;
  }
  .side-stripe {
    position: absolute; left: 90px; top: 0; width: 22px; height: 248px;
    background: var(--stone);
  }
  .reminder { position: absolute; left: 122px; top: 0; width: 266px; height: 248px; font-size: 13px; }
  .reminder .label { position: absolute; text-align: center; }
  .reminder .rule { position: absolute; height: 1px; background: var(--ink); }
  .reminder .note {
    position: absolute; left: 0; width: 266px; text-align: center;
    font-size: 13.5px; white-space: nowrap;
  }
  .reminder .phone {
    position: absolute; left: 0; width: 266px; text-align: center; top: 200px;
    font-size: 21px; white-space: nowrap;
  }

  /* Front side: practice details */
  .card-front { position: absolute; left: 787px; top: 0; width: 390px; height: 248px; }
  .brand-bar {
    position: absolute; left: 0; top: 8px; width: 390px; height: 62px;
    background: var(--blush);
  }
  .brand-bar .brand {
    position: absolute; right: 18px; top: 14px;
    color: var(--paper); font-size: 38px; line-height: 1;
  }
  .brand-bar .dot {
    position: absolute; right: 4px; top: 6px; width: 10px; height: 10px;
    border-radius: 50%; background: var(--stone);
  }
  .accent-bar {
    position: absolute; left: 0; top: 81px; width: 390px; height: 16px;
    background: var(--stone);
  }
  .doctor {
    position: absolute; left: 0; top: 110px; line-height: 21px;
  }
  .doctor .name { font-size: 15px; }
  .doctor .title { font-size: 11.5px; }
  .details {
    position: absolute; right: 0; top: 108px; text-align: right;
    font-size: 11.5px; line-height: 21px; font-style: normal; white-space: nowrap;
  }
  .details .web { margin-top: 18px; line-height: 25px; font-size: 12px; }
</style>
</head>
<body>
<main class="sheet">

  <section class="card-back" aria-label="Appointment reminder">
    <div class="side-band">
      <span class="dot"></span>
      <span class="brand">She Glow</span>
    </div>
    <div class="side-stripe"></div>

    <div class="reminder">
      <span class="label" style="left:0;width:266px;top:19px;">Appointment for:</span>
      <span class="rule" style="left:6px;width:252px;top:70px;"></span>

      <span class="label" style="left:6px;width:114px;top:84px;">Date:</span>
      <span class="label" style="left:150px;width:112px;top:84px;">Time:</span>
      <span class="rule" style="left:6px;width:114px;top:121px;"></span>
      <span class="rule" style="left:146px;width:116px;top:121px;"></span>

      <p class="note" style="top:139px;">If you are unable to keep your appointment</p>
      <p class="note" style="top:166px;">please contact us as soon as possible</p>
      <p class="phone">877-SHE-GLOW(743-4569)</p>
    </div>
  </section>

  <section class="card-front" aria-label="Practice details">
    <div class="brand-bar">
      <span class="brand">She Glow</span>
      <span class="dot"></span>
    </div>
    <div class="accent-bar"></div>

    <div class="doctor">
      <div class="name">Dr. Delphine Corvessa</div>
      <div class="title">Obstetrics &amp; Gynecology</div>
    </div>

    <address class="details">
      <div>SHE Glow</div>
      <div>618 Larkspur Road Suite 412</div>
      <div>Nashville TN</div>
      <div class="web">
        <div>tbrevinshaw@mailpost.example</div>
        <div>tristarveloragentle.example</div>
      </div>
    </address>
  </section>

</main>
</body>
</html>
```